Healthy Supplement featuring Moringa products

Need 3 business card options for our reps to order from Cardloom. Our reps will be ordering from Cardloom once we upload them. Attached is our current designs to show what info needs to be on the cards. Our website is www.tkvitality.com
The business cards will be a template for our reps to order from. Most of our reps are Asian & Hispanic. Please look at our website so you can see who we are to get the look and feel what we need.
Target Market(s)
Adults 30 on up. Health oriented people.
Industry/Entity Type
Health And Wellness
Contact Information for Business Card
Name
Title
Phone
Logo
www.tkvitality.com/my/username
Font styles to use
Requirements
Must have
- Please match our website look and colors. A moringa leaf is nice, but am open to something different.
Nice to have
- Healthy looking and warm, not super cold or too modern.
Should not have
- No harsh colors please.

```html
<!DOCTYPE html>
<html lang="en">
<head>
<meta charset="utf-8">
<title>TK Vitality – Business Card</title>
<link href="https://fonts.googleapis.com/css2?family=Montserrat:wght@400;500;600&display=swap" rel="stylesheet">
<style>
  :root {
    --page: #e8e5df;
    --card-dark: #1b1c1e;
    --leaf-green: #7dba1c;
    --leaf-green-light: #93cc1a;
    --leaf-green-deep: #64a50f;
    --warm-orange: #f59a23;
    --ink: #1b1c1e;
    --text-light: #eef0ea;
    --rule: #6a6c6e;
  }
  * { margin: 0; padding: 0; box-sizing: border-box; }
  html, body {
    width: 1125px; height: 1200px; overflow: hidden;
    background: var(--page);
    font-family: "Montserrat", sans-serif;
  }
  .canvas { position: relative; width: 1125px; height: 1200px; }

  .card {
    position: absolute; left: 150px; width: 825px; height: 470px;
    box-shadow: 0 4px 10px rgba(0,0,0,.25);
    overflow: hidden;
  }

  /* Front */
  .card--front { top: 99px; background: var(--card-dark); }
  .brand-mark {
    position: absolute; right: 55px; top: 120px;
    color: var(--leaf-green); font-weight: 600; font-size: 38px;
    letter-spacing: 1px;
  }
  .rep-name {
    position: absolute; left: 49px; top: 268px;
    color: var(--leaf-green); font-weight: 600; font-size: 31px;
  }
  .rep-title {
    position: absolute; left: 49px; top: 306px;
    color: var(--warm-orange); font-weight: 500; font-size: 21px;
  }
  .divider {
    position: absolute; left: 51px; right: 56px; top: 345px;
    height: 1px; background: var(--rule);
  }
  .contact-list {
    position: absolute; left: 51px; top: 366px; list-style: none;
    color: var(--text-light); font-size: 19px; line-height: 27px;
  }
  .contact-list li { display: flex; align-items: center; gap: 14px; }
  .contact-list svg { width: 18px; height: 18px; fill: var(--leaf-green); }
  .social-slots {
    position: absolute; right: 53px; top: 374px; display: flex; gap: 4px;
  }
  .social-slots span {
    width: 33px; height: 33px; border-radius: 50%;
    border: 1.5px solid var(--leaf-green);
  }
  .accent-stripe { position: absolute; left: 0; bottom: 0; width: 825px; height: 8px; }

  /* Back */
  .card--back {
    top: 632px;
    background: radial-gradient(ellipse at 50% 25%, var(--leaf-green-light) 0%, var(--leaf-green) 50%, var(--leaf-green-deep) 100%);
  }
  .brand-mark--large {
    position: absolute; left: 0; right: 0; top: 170px; text-align: center;
    color: var(--ink); font-weight: 600; font-size: 72px; letter-spacing: 2px;
  }
  .website {
    position: absolute; left: 0; right: 0; top: 388px; text-align: center;
    color: var(--ink); font-weight: 500; font-size: 21px; letter-spacing: 6px;
  }
</style>
</head>
<body>
<div class="canvas">

  <section class="card card--front">
    <div class="brand-mark">TK Vitality</div>

    <div class="rep-name">Daniel Reyes</div>
    <div class="rep-title">President</div>
    <div class="divider"></div>

    <ul class="contact-list">
      <li>
        <svg viewBox="0 0 24 24" aria-hidden="true"><path d="M6.6 10.8a15.1 15.1 0 0 0 6.6 6.6l2.2-2.2c.3-.3.7-.4 1-.2 1.1.4 2.3.6 3.6.6.6 0 1 .4 1 1V20c0 .6-.4 1-1 1C10.6 21 3 13.4 3 4c0-.6.4-1 1-1h3.5c.6 0 1 .4 1 1 0 1.3.2 2.5.6 3.6.1.3 0 .7-.2 1z"/></svg>
        <span>+1(555)214-0387</span>
      </li>
      <li>
        <svg viewBox="0 0 24 24" aria-hidden="true"><path d="M3 6h18v12H3z" opacity=".0"/><path d="M3 6l9 6 9-6v12H3z"/><path d="M3 5h18l-9 6z"/></svg>
        <span>info@tkvitality.com</span>
      </li>
    </ul>

    <div class="social-slots" aria-hidden="true">
      <span></span><span></span><span></span><span></span>
    </div>

    <svg class="accent-stripe" viewBox="0 0 825 8" preserveAspectRatio="none" aria-hidden="true">
      <polygon points="0,0 524,0 519,8 0,8" fill="var(--leaf-green)"/>
      <polygon points="529,0 825,0 825,8 524,8" fill="var(--warm-orange)"/>
    </svg>
  </section>

  <section class="card card--back">
    <div class="brand-mark--large">TK Vitality</div>
    <div class="website">WWW.TKVITALITY.COM</div>
  </section>

</div>
</body>
</html>
```